Vantor Scorecard

Redesign KLT's existing Vantor scorecard, which tracks and reports key performance indicators (KPIs) for our clients. The scorecard provides our customers with an at-a-glance view of our on-site performance. Vantor is a tool that automatically populates and reports this data.

Review the attached document and deliver suggested redesign options for the two attached views.
Page 1: Portfolio-wide views (high level rollup of multiple sites)
Page 2: Site-level view
Updates

Project Deadline Extended
Reason: Due to the holiday season within the U.S. around the globe we have decided to extend out deadline in hopes of gaining more participation. We will also be providing comments to the current designs tomorrow.

Font styles to use
Sans Serif

Requirements
Must have
• - Sans serif fonts
- Clean aesthetic
- Utilize the exact key performance indicators as are in the attached mockup
- White background (think Plum-esque)
Nice to have
• - Ideas for animation of design elements
Should not have
• - Pictures (icons are okay)

```html
<!DOCTYPE html>
<html lang="en">
<head>
<meta charset="utf-8">
<title>Scorecard – KPI Score Details</title>
<link rel="stylesheet" href="https://fonts.googleapis.com/css2?family=Aleo:ital,wght@0,300;0,400;1,300;1,700&family=Lato:ital,wght@0,400;1,400&display=swap">
<style>
  :root {
    --plum: #7c4a67;
    --plum-bar: #cdb5c3;
    --plum-bar-soft: #e7dde2;
    --ink-grey: #7a7a7a;
    --logo-grey: #c9c9c9;
    --axis-ink: #444;
    --grid: #e3e3e3;
    --pie-rest: #e4e4e4;
    --paper: #ffffff;
  }
  * { margin: 0; padding: 0; box-sizing: border-box; }
  html, body { width: 1200px; height: 675px; overflow: hidden; background: var(--paper); }
  .canvas { position: relative; width: 1200px; height: 675px; overflow: hidden; background: var(--paper); font-family: "Aleo", serif; }

  .brand-slot { position: absolute; font-family: "Aleo", serif; font-weight: 300; font-style: italic; font-size: 24px; color: var(--logo-grey); }
  .brand-slot--left { left: 143px; top: 29px; }
  .brand-slot--right { left: 1015px; top: 26px; }

  .main-nav { position: absolute; left: 2px; right: 0; top: 88px; height: 47px; background: var(--paper); box-shadow: 0 0 5px rgba(0,0,0,.28); }
  .main-nav__item { position: absolute; top: 0; height: 47px; line-height: 47px; transform: translateX(-50%); font-weight: 300; font-size: 21px; color: var(--plum); white-space: nowrap; }
  .main-nav__item--active { left: 8px; top: 4px; width: 170px; height: 39px; line-height: 39px; transform: none; text-align: center; background: var(--plum); color: var(--paper); }

  .page-heading { position: absolute; left: 54px; top: 181px; line-height: 1.16; }
  .page-heading__section { font-style: italic; font-weight: 700; font-size: 28px; color: var(--plum); }
  .page-heading__title { font-style: italic; font-weight: 700; font-size: 28px; color: var(--ink-grey); }
  .page-heading__period { font-style: italic; font-weight: 300; font-size: 28px; color: var(--ink-grey); }

  .site-score__caption { position: absolute; left: 878px; top: 205px; text-align: left; font-style: italic; font-weight: 300; font-size: 17px; line-height: 23px; color: var(--ink-grey); }
  .site-score__chart { position: absolute; left: 984px; top: 169px; }
  .site-score__value { position: absolute; left: 1052px; top: 246px; transform: translateX(-50%); font-style: italic; font-weight: 300; font-size: 32px; color: var(--paper); }

  .kpi-chart { position: absolute; left: 0; top: 0; }
  .kpi-chart__grid line { stroke: var(--grid); stroke-width: 1; }
  .kpi-chart__axis text { font-family: "Lato", sans-serif; font-style: italic; font-size: 15px; fill: var(--axis-ink); text-anchor: end; }
  .bar { fill: var(--plum-bar-soft); }
  .bar--top { fill: var(--plum-bar); }
  .kpi-chart__labels text { font-family: "Lato", sans-serif; font-style: italic; font-size: 10px; fill: var(--axis-ink); text-anchor: end; }
</style>
</head>
<body>
<div class="canvas">
  <div class="brand-slot brand-slot--left">Logo Here</div>
  <div class="brand-slot brand-slot--right">Logo Here</div>

  <nav class="main-nav">
    <span class="main-nav__item main-nav__item--active">Governance</span>
    <span class="main-nav__item" style="left:251px">Cost</span>
    <span class="main-nav__item" style="left:394px">Quality</span>
    <span class="main-nav__item" style="left:543px">EHS</span>
    <span class="main-nav__item" style="left:683px">Personnel</span>
    <span class="main-nav__item" style="left:829px">Scorecard</span>
    <span class="main-nav__item" style="left:973px">Innovations</span>
    <span class="main-nav__item" style="left:1122px">Updates</span>
  </nav>

  <header class="page-heading">
    <div class="page-heading__section">Scorecard</div>
    <div class="page-heading__title">KPI Score Details</div>
    <div class="page-heading__period">July 2013</div>
  </header>

  <div class="site-score__caption">Site Score<br>Gole is 90%</div>
  <svg class="site-score__chart" width="132" height="132" viewBox="984 169 132 132" aria-label="Site score 86% of 90% goal">
    <circle cx="1050" cy="235" r="66" fill="var(--plum)"/>
    <path d="M1050 235 L1084 178.4 A66 66 0 0 1 1115.2 224.7 Z" fill="var(--pie-rest)"/>
  </svg>
  <div class="site-score__value">86%</div>

  <svg class="kpi-chart" width="1200" height="675" viewBox="0 0 1200 675" aria-label="KPI score details bar chart">
    <g class="kpi-chart__grid">
      <line x1="173" y1="326" x2="1024" y2="326"/>
      <line x1="173" y1="378.7" x2="1024" y2="378.7"/>
      <line x1="173" y1="431.4" x2="1024" y2="431.4"/>
      <line x1="173" y1="484.1" x2="1024" y2="484.1"/>
      <line x1="173" y1="536.8" x2="1024" y2="536.8"/>
      <line x1="173" y1="589.5" x2="1024" y2="589.5"/>
    </g>
    <g class="kpi-chart__axis">
      <text x="161" y="332">100%</text>
      <text x="161" y="384.7">90%</text>
      <text x="161" y="437.4">80%</text>
      <text x="161" y="490.1">70%</text>
      <text x="161" y="542.8">60%</text>
      <text x="161" y="595.5">50%</text>
    </g>
    <g class="kpi-chart__bars">
      <rect class="bar" x="197" y="436.7" width="14" height="152.8"/>
      <rect class="bar" x="224" y="389.2" width="14" height="200.3"/>
      <rect class="bar" x="251" y="399.8" width="14" height="189.7"/>
      <rect class="bar" x="278" y="463" width="14" height="126.5"/>
      <rect class="bar bar--top" x="305" y="355" width="14" height="234.5"/>
      <rect class="bar" x="332" y="415.6" width="14" height="173.9"/>
      <rect class="bar" x="359" y="436.7" width="14" height="152.8"/>
      <rect class="bar" x="386" y="431.4" width="14" height="158.1"/>
      <rect class="bar" x="413" y="399.8" width="14" height="189.7"/>
      <rect class="bar bar--top" x="440" y="344.4" width="14" height="245.1"/>
      <rect class="bar" x="467" y="463" width="14" height="126.5"/>
      <rect class="bar" x="494" y="415.6" width="14" height="173.9"/>
      <rect class="bar" x="521" y="413" width="14" height="176.5"/>
      <rect class="bar" x="548" y="389.2" width="14" height="200.3"/>
      <rect class="bar" x="575" y="389.2" width="14" height="200.3"/>
      <rect class="bar" x="602" y="399.8" width="14" height="189.7"/>
      <rect class="bar" x="629" y="415.6" width="14" height="173.9"/>
      <rect class="bar bar--top" x="656" y="344.4" width="14" height="245.1"/>
      <rect class="bar" x="683" y="436.7" width="14" height="152.8"/>
      <rect class="bar" x="710" y="386.6" width="14" height="202.9"/>
      <rect class="bar" x="737" y="389.2" width="14" height="200.3"/>
      <rect class="bar bar--top" x="764" y="331.3" width="14" height="258.2"/>
      <rect class="bar" x="791" y="399.8" width="14" height="189.7"/>
      <rect class="bar bar--top" x="818" y="341.8" width="14" height="247.7"/>
      <rect class="bar" x="845" y="415.6" width="14" height="173.9"/>
      <rect class="bar bar--top" x="872" y="355" width="14" height="234.5"/>
      <rect class="bar" x="899" y="402.4" width="14" height="187.1"/>
      <rect class="bar bar--top" x="926" y="326" width="14" height="263.5"/>
      <rect class="bar" x="953" y="434" width="14" height="155.5"/>
      <rect class="bar" x="980" y="381.3" width="14" height="208.2"/>
    </g>
    <g class="kpi-chart__labels">
      <text transform="translate(208 601) rotate(-40)">Lorem - ipsum</text>
      <text transform="translate(235 601) rotate(-40)">Dolor - sit</text>
      <text transform="translate(262 601) rotate(-40)">Lorem - ipsum</text>
      <text transform="translate(289 601) rotate(-40)">Title - text</text>
      <text transform="translate(316 601) rotate(-40)">Dolor - sit</text>
      <text transform="translate(343 601) rotate(-40)">Text - text</text>
      <text transform="translate(370 601) rotate(-40)">Lorem - ipsum</text>
      <text transform="translate(397 601) rotate(-40)">Dolor - sit</text>
      <text transform="translate(424 601) rotate(-40)">Lorem - ipsum</text>
      <text transform="translate(451 601) rotate(-40)">Title - text</text>
      <text transform="translate(478 601) rotate(-40)">Dolor - sit</text>
      <text transform="translate(505 601) rotate(-40)">Text - text</text>
      <text transform="translate(532 601) rotate(-40)">Lorem - ipsum</text>
      <text transform="translate(559 601) rotate(-40)">Dolor - sit</text>
      <text transform="translate(586 601) rotate(-40)">Lorem - ipsum</text>
      <text transform="translate(613 601) rotate(-40)">Title - text</text>
      <text transform="translate(640 601) rotate(-40)">Dolor - sit</text>
      <text transform="translate(667 601) rotate(-40)">Text - text</text>
      <text transform="translate(694 601) rotate(-40)">Lorem - ipsum</text>
      <text transform="translate(721 601) rotate(-40)">Dolor - sit</text>
      <text transform="translate(748 601) rotate(-40)">Lorem - ipsum</text>
      <text transform="translate(775 601) rotate(-40)">Title - text</text>
      <text transform="translate(802 601) rotate(-40)">Dolor - sit</text>
      <text transform="translate(829 601) rotate(-40)">Text - text</text>
      <text transform="translate(856 601) rotate(-40)">Lorem - ipsum</text>
      <text transform="translate(883 601) rotate(-40)">Dolor - sit</text>
      <text transform="translate(910 601) rotate(-40)">Title - text</text>
      <text transform="translate(937 601) rotate(-40)">Dolor - sit</text>
      <text transform="translate(964 601) rotate(-40)">Title - text</text>
      <text transform="translate(991 601) rotate(-40)">Lorem - ipsum</text>
    </g>
  </svg>
</div>
</body>
</html>
```